Book Cover for Memoir: Sexual Assault and Traumatic Stress

I need a cover design for a memoir that is a victim's story of a sexual assault. I will need a print-on-demand cover, an eBook cover, and a 3D thumbnail image. The thumbnail and eBook cover will be used immediately, and the POD cover will be used in a few months with the full manuscript is ready. Therefore, I need an artist who is willing to make small adjustments if needed once the page count is set.

I have a image I have purchased that should give you an idea of the desired direction, but you can feel free to use your own images. I have attached some examples of book covers I like. I attached a color palette for fonts.

Overall Look: Fonts should be feminine and thin, but large to stand out. Look should be simple and elegant, and display and overall depressing feeling. There should be enough detail though to make it look professionally put together. Not TOO minimalistic.

I have also attached the Print Harbor templates if you choose to use those. If not, ensure there is an open place for the barcode on the bottom right.

Requirements
Must have
• Title: Beneath Quiet Rain
Subtitle: One Woman's Account of Fear, Guilt & Silence
Author: Dana Ruth Whitford
Audience: Mostly women 18-30
Quote (for the back): "I always thought I'd know how I'd react if I ever was raped. I was wrong. I've been wrong a lot lately."
Summary (back cover): When twenty-seven-year-old Dana Whitford wakes up with a gut-wrenching feeling, she has little memory of the horrifying events that occurred the night before. Days earlier, Dana was a spirited single mom who had abandoned her hometown to raise her daughter in the city and pursue her dreams. In the short months since Dana’s move to Seattle, she became the adored lover of a charismatic lawyer, started a new business, and finally felt life was going her way. So what happened to cause her to break?

In a gripping and heartbreaking narrative, Dana tells the true story of how her life unraveled from the traumatic events that took place that night and why what seems obvious to everyone else is impossible for Dana to believe. Beneath Quiet Rain is a chilling exploration of memory through trauma, trust in humanity, and a captivating story of strength and survival that appeals to the heart of fathers and mothers, sons and daughters, and men and women alike.
Nice to have
• BACK COVER: I'd like to have a photo on the back. This should depict the happy life of the main character before the sexual assault, and should be with her daughter. Or should be a nature scene that starts at the corner and blends into the rest of the cover. I have attached a possible image or you can use something you like.

```html
<!DOCTYPE html>
<html lang="en">
<head>
<meta charset="utf-8">
<title>Beneath Quiet Rain – Cover Wrap</title>
<link rel="stylesheet" href="https://fonts.googleapis.com/css2?family=Arimo:wght@400&display=swap">
<style>
  :root {
    --ink-purple: #4a1f63;
    --band-purple: #5b2a7a;
    --smoke-purple: #6e4a8c;
    --paper: #ffffff;
    --sheet: #f1eef4;
    --outline-grey: #b9b3bf;
  }
  * { margin: 0; padding: 0; box-sizing: border-box; }
  html, body { width: 1200px; height: 848px; overflow: hidden; background: var(--paper); }
  body { font-family: "Arimo", Arial, sans-serif; }
  .wrap { position: relative; width: 1200px; height: 848px; background: var(--paper); overflow: hidden; }

  /* Back cover */
  .back { position: absolute; left: 0; top: 0; width: 556px; height: 848px; }
  .back-photo {
    position: absolute; left: 0; top: 440px; width: 556px; height: 408px;
    background: radial-gradient(ellipse at 40% 75%, #dcd8d6 0%, #ebe8e7 45%, rgba(255,255,255,0) 80%),
                linear-gradient(180deg, rgba(255,255,255,0) 0%, #f2f0ef 55%, #f7f6f6 100%);
  }
  .back-summary {
    position: absolute; left: 22px; top: 40px; width: 512px;
    color: var(--ink-purple); font-size: 18.6px; line-height: 24.4px; text-align: center;
  }
  .back-summary p + p { margin-top: 24px; }

  /* Spine */
  .spine { position: absolute; left: 556px; top: 0; width: 80px; height: 848px; background: var(--paper); }
  .spine-title, .spine-author {
    position: absolute; left: 50%; transform: translateX(-50%);
    writing-mode: vertical-rl; color: var(--ink-purple); white-space: nowrap; line-height: 1;
  }
  .spine-title { top: 24px; font-size: 40px; }
  .spine-author { top: 522px; font-size: 34px; }

  /* Front cover */
  .front { position: absolute; left: 636px; top: 0; width: 564px; height: 848px; overflow: hidden; }
  .front-photo {
    position: absolute; inset: 0;
    background:
      radial-gradient(ellipse at 55% 28%, #c9a79b 0%, #a77f7a 18%, rgba(110,74,140,0) 45%),
      linear-gradient(180deg, var(--smoke-purple) 0%, #8d6fa5 30%, #b7a6c4 48%, var(--sheet) 62%, #f6f4f8 100%);
  }
  .front-author {
    position: absolute; top: 28px; left: 0; width: 100%; text-align: center;
    color: var(--paper); font-size: 42px; letter-spacing: 0.5px;
  }
  .title-big {
    position: absolute; left: 0; top: 490px; width: 100%; text-align: center;
    font-size: 215px; line-height: 1; letter-spacing: 2px;
    transform: scaleY(1.35); transform-origin: top center;
    color: rgba(255,255,255,0.85);
    -webkit-text-stroke: 1.5px var(--outline-grey);
  }
  .title-band { position: absolute; left: 0; top: 440px; width: 564px; height: 100px; }
  .title-top {
    position: absolute; left: 0; top: 455px; width: 100%; text-align: center;
    color: var(--paper); font-size: 56px; letter-spacing: 1px; line-height: 1;
  }
  .subtitle {
    position: absolute; left: 0; top: 770px; width: 100%; text-align: center;
    color: var(--ink-purple); font-size: 20.5px;
  }
</style>
</head>
<body>
<div class="wrap">

  <section class="back">
    <div class="back-photo" role="img" aria-label="Soft faded photograph of a smiling mother with her young child"></div>
    <div class="back-summary">
      <p>When twenty-seven-year-old Dana Whitford wakes up with a gut-wrenching feeling, she has little memory of the horrifying events that occurred the night before. Days earlier, Dana was a spirited single mom who had abandoned her hometown to raise her daughter in the city and pursue her dreams. In the short months since Dana’s move to Seattle, she became the adored lover of a charismatic lawyer, started a new business, and finally felt life was going her way. So what happened to cause her to break?</p>
      <p>In a gripping and heartbreaking narrative, Dana tells the true story of how her life unraveled from the traumatic events that took place that night and why what seems obvious to everyone else is impossible for Dana to believe. Beneath Quiet Rain is a chilling exploration of memory through trauma, trust in humanity, and a captivating story of strength and survival that appeals to the heart of fathers and mothers, sons and daughters, and men and women alike.</p>
    </div>
  </section>

  <section class="spine">
    <div class="spine-title">BENEATH QUIET RAIN</div>
    <div class="spine-author">D. R. WHITFORD</div>
  </section>

  <section class="front">
    <div class="front-photo" role="img" aria-label="Photograph of a woman sitting on white sheets hugging her knees, head bowed, in purple smoke"></div>
    <div class="front-author">DANA RUTH WHITFORD</div>
    <div class="title-big">RAIN</div>

    <svg class="title-band" viewBox="0 0 564 100" aria-hidden="true">
      <polygon fill="#ffffff" points="0,8 20,4 38,9 60,3 85,8 110,2 140,7 170,3 200,8 232,2 262,7 290,3 320,9 352,4 382,8 410,2 440,7 470,3 500,8 530,3 564,7 564,96 540,92 512,97 482,91 452,96 420,92 390,98 360,91 330,96 300,92 270,97 240,91 210,96 180,92 150,97 120,91 90,96 60,92 30,97 0,92"/>
      <polygon fill="var(--band-purple)" points="0,15 25,12 50,16 78,11 105,15 135,10 165,15 195,11 225,16 255,11 285,15 315,10 345,15 375,12 405,16 435,11 465,15 495,10 525,15 564,12 564,86 535,89 505,84 475,89 445,85 415,90 385,84 355,89 325,85 295,90 265,84 235,89 205,85 175,90 145,84 115,89 85,85 55,90 25,85 0,88"/>
    </svg>
    <div class="title-top">BENEATH QUIET</div>
    <div class="subtitle">One Woman's Account of Fear, Guilt &amp; Silence</div>
  </section>

</div>
</body>
</html>
```